Create branded design templates/backgrounds for social media based on UK property investing company

I'd like Instagram, Facebook and Linkedin backgrounds/templates to add text to, based on my logo design and business of UK holiday let investing. Ideally I'd have some base designs for me to approve, then engage with the winning designer further to create about 50 different templates. I looking for a mixture of templates with the logo and using logo colours, others of internal holiday let photos including logos and a few of my photo imposed on the front of them.
Updates

Slow in providing feedback

Target Market(s)

Middle aged adults

Industry/Entity Type

Holiday let properties

Requirements
Must have
• a distinct brand look that can be replicated

```html
<!DOCTYPE html>
<html lang="en">
<head>
<meta charset="utf-8">
<title>Harbourstay – Instagram post templates</title>
<link rel="stylesheet" href="https://fonts.googleapis.com/css2?family=Open+Sans:wght@600;700&display=swap">
<style>
  :root {
    --brand-blue: #0686d2;
    --brand-green: #5aaa0a;
    --brand-yellow: #f8d832;
    --brand-navy: #0d3a5c;
    --paper: #ffffff;
    --photo-light: #c9b8a8;
    --photo-dark: #5b5a54;
    --caption: #111111;
  }
  * { box-sizing: border-box; margin: 0; padding: 0; }
  html, body { width: 1200px; height: 675px; overflow: hidden; background: var(--paper); }
  body { position: relative; font-family: "Open Sans", Arial, sans-serif; }

  .template {
    position: absolute;
    width: 249px;
    height: 249px;
    overflow: hidden;
    box-shadow: 0 4px 8px rgba(0,0,0,0.22);
  }
  .template--yellow { background: var(--brand-yellow); }
  .template--white { background: var(--paper); }
  .template--blue { background: var(--brand-blue); }
  .template--green { background: var(--brand-green); }

  .col-1 { left: 67.5px; } .col-2 { left: 339.5px; } .col-3 { left: 611.5px; } .col-4 { left: 883px; }
  .row-1 { top: 77px; } .row-2 { top: 349px; }

  .portrait {
    position: absolute;
    left: 0; top: 92px;
    width: 170px; height: 157px;
    border-radius: 70px 70px 0 0;
    background: linear-gradient(180deg, var(--photo-light) 0%, var(--photo-light) 55%, var(--photo-dark) 100%);
  }

  .bubble { position: absolute; left: 0; top: 0; width: 249px; height: 249px; }

  .bubble-text {
    position: absolute;
    font-weight: 600;
    font-size: 10.6px;
    line-height: 13.8px;
  }
  .bubble-text--right { right: 38px; top: 64px; text-align: right; color: var(--paper); }
  .bubble-text--left { left: 99px; top: 67px; }
  .bubble-text--green { color: #2f7a0a; }
  .bubble-text--navy { color: var(--brand-navy); }
  .template--green .bubble-text--left { left: 99px; }

  .headline {
    position: absolute;
    left: 17px; top: 13px;
    font-weight: 600;
    font-size: 18.6px;
    line-height: 22.1px;
  }
  .headline--dark { color: var(--brand-navy); }
  .headline--light { color: var(--paper); }
  .headline .accent { color: var(--brand-blue); }

  .brand-name {
    position: absolute;
    display: flex;
    align-items: center;
    gap: 4px;
    font-weight: 700;
    font-size: 12px;
    line-height: 1;
  }
  .brand-name .dot { width: 7px; height: 7px; }
  .brand-name--bottom-right { right: 16px; bottom: 18px; }
  .brand-name--bottom-left { left: 16px; bottom: 18px; }
  .brand-name--top-left { left: 9px; top: 22px; }
  .brand-name--white { color: var(--paper); }
  .brand-name--white .dot { background: var(--paper); }
  .brand-name--blue { color: var(--brand-blue); }
  .brand-name--blue .dot { background: var(--brand-blue); }

  .caption {
    position: absolute;
    left: 67px; top: 624px;
    font-family: Arial, Helvetica, sans-serif;
    font-size: 14.5px;
    color: var(--caption);
  }
</style>
</head>
<body>

  <!-- Row 1 -->
  <section class="template template--yellow col-1 row-1">
    <div class="portrait" role="img" aria-label="Portrait photo of the company founder"></div>
    <svg class="bubble" viewBox="0 0 249 249" aria-hidden="true">
      <polygon points="78,57 153,17 228,57 228,164 124,164 92,188 78,164" fill="var(--brand-blue)"/>
    </svg>
    <p class="bubble-text bubble-text--right">Lorem ipsum dolor sit<br>amet, consectetur<br>adipiscing elit, sed do<br>eiusmod tempor<br>incididunt ut labore et<br>dolore magna aliqua.</p>
    <div class="brand-name brand-name--top-left brand-name--white"><span class="dot"></span>Harbourstay</div>
  </section>

  <section class="template template--white col-2 row-1">
    <div class="portrait" role="img" aria-label="Portrait photo of the company founder"></div>
    <svg class="bubble" viewBox="0 0 249 249" aria-hidden="true">
      <polygon points="78,57 153,17 228,57 228,164 124,164 92,188 78,164" fill="var(--brand-blue)"/>
    </svg>
    <p class="bubble-text bubble-text--right">Lorem ipsum dolor sit<br>amet, consectetur<br>adipiscing elit, sed do<br>eiusmod tempor<br>incididunt ut labore et<br>dolore magna aliqua.</p>
    <div class="brand-name brand-name--bottom-right brand-name--blue"><span class="dot"></span>Harbourstay</div>
  </section>

  <section class="template template--white col-3 row-1">
    <h2 class="headline headline--dark">Lorem ipsum dolor<br>sit amet, consectetur<br>adipiscing elit, sed<br>do eiusmod tempor<br>incididunt ut <span class="accent">labore<br>et dolore magna</span><br>aliqua.</h2>
    <div class="brand-name brand-name--bottom-right brand-name--blue"><span class="dot"></span>Harbourstay</div>
  </section>

  <section class="template template--white col-4 row-1">
    <h2 class="headline headline--dark">Lorem ipsum dolor<br>sit amet, consectetur<br>adipiscing elit, sed<br>do eiusmod tempor<br>incididunt ut <span class="accent">labore<br>et dolore magna</span><br>aliqua.</h2>
    <div class="brand-name brand-name--bottom-right brand-name--blue"><span class="dot"></span>Harbourstay</div>
  </section>

  <!-- Row 2 -->
  <section class="template template--blue col-1 row-2">
    <h2 class="headline headline--light">Lorem ipsum dolor<br>sit amet, consectetur<br>adipiscing elit, sed<br>do eiusmod tempor<br>incididunt ut labore<br>et dolore magna<br>aliqua.</h2>
    <div class="brand-name brand-name--bottom-right brand-name--white"><span class="dot"></span>Harbourstay</div>
  </section>

  <section class="template template--blue col-2 row-2">
    <svg class="bubble" viewBox="0 0 249 249" aria-hidden="true">
      <polygon points="83,57 158,16 233,57 233,163 122,163 83,193" fill="var(--paper)"/>
    </svg>
    <p class="bubble-text bubble-text--left bubble-text--green">Lorem ipsum dolor sit<br>amet, consectetur<br>adipiscing elit, sed do<br>eiusmod tempor<br>incididunt ut labore et<br>dolore magna aliqua.</p>
    <div class="brand-name brand-name--bottom-left brand-name--white"><span class="dot"></span>Harbourstay</div>
  </section>

  <section class="template template--green col-3 row-2">
    <h2 class="headline headline--light">Lorem ipsum dolor<br>sit amet, consectetur<br>adipiscing elit, sed<br>do eiusmod tempor<br>incididunt ut labore<br>et dolore magna<br>aliqua.</h2>
    <div class="brand-name brand-name--bottom-right brand-name--white"><span class="dot"></span>Harbourstay</div>
  </section>

  <section class="template template--green col-4 row-2">
    <svg class="bubble" viewBox="0 0 249 249" aria-hidden="true">
      <polygon points="83,57 158,16 233,57 233,163 122,163 83,193" fill="var(--paper)"/>
    </svg>
    <p class="bubble-text bubble-text--left bubble-text--navy">Lorem ipsum dolor sit<br>amet, consectetur<br>adipiscing elit, sed do<br>eiusmod tempor<br>incididunt ut labore et<br>dolore magna aliqua.</p>
    <div class="brand-name brand-name--bottom-left brand-name--white"><span class="dot"></span>Harbourstay</div>
  </section>

  <p class="caption">instagram post template example</p>

</body>
</html>
```